Design Brief – Premium Vehicle Wrap for KT TX. Mylo Cargo

Details
I'm looking for a high-end, premium vehicle wrap for my new KT TX. Mylo Cargo that reflects the quality and craftsmanship of my business. WWW.MERVALLE-EXAMPLE.CO.UK

Brand:
MERVALLE
Kitchens • Bedrooms • Bathrooms

Our market and product sits just above the large retail chains in terms of quality and price, but below luxury independents, so the design should feel modern, sophisticated, clean and aspirational rather than loud or cluttered.

Design Direction
Premium, minimalist aesthetic.
Predominantly deep navy (preferably matt if it works) combined with the van's original Candy white, using a fade, split or flowing transition. The front should retain more white, (as it is difficult to wrap the front grill) , blending into navy towards the rear. This can also be split top to bottom maybe? Brand colours are dark navy and light grey (silver accents could work

I'd like the wrap to incorporate high-quality lifestyle imagery of a beautiful kitchen, bathroom (and, if it works, also a bedroom). Images should blend naturally into the design rather than looking like stickers.

Information to Include
MERVALLE logo
Design - Supply - Install
Website
Phone number
Email address
QR code to book a survey (space allocated if required)
Social icons if they enhance the design
Fendra 5* Reviews logo

Style
Think premium automotive branding rather than traditional signwriting. I want people to think "quality interior specialist" and "better than the mainstream" when they see the van.

Please avoid overly busy graphics, excessive text or generic swooshes. Clean lines, negative space and subtle detail are preferred.

Feel free to be creative with the layout, provided the design remains elegant and highly legible from a distance. I'd welcome concepts that use the shape of the TX. Mylo to create something unique rather than simply wrapping every panel.

The finished design should look as though it belongs outside nice homes and premium developments, while remaining memorable and instantly recognisable.

Target Market(s)

Homeowners that want quality just above the mainstream/big chains, but prices below the high end luxury independents

Industry/Entity Type

Kitchens Bedrooms and Bathrooms. Design, supply and install

Font styles to use
Serif
Sans Serif

Colors
0054AA
0677BA
7BADD7
CADEEF
E8F1F8

Requirements
Must have
• Premium, high-end design that reflects a quality interiors brand. Designed specifically for a KT TX. Mylo Cargo. MERVALLE logo prominently displayed. "Kitchens • Bedrooms • Bathrooms" clearly visible. Space for website, phone number, email and QR code. Predominantly deep navy with the original white of the van incorporated into the design. Smooth fade or two-tone transition between navy and white. High-quality imagery of a kitchen and bathroom (bedroom optional if it complements the design). Easily readable from a distance. Full wrap design including both sides, rear and bonnet/front where appropriate.
Nice to have
• Matt navy finish. Creative use of the TX. Mylo body lines. Luxury, architectural feel rather than a typical sign-written van. Images blended seamlessly into the design rather than boxed photographs. Subtle textures or gradients. Silver accent details if they complement the design. A design that looks equally good parked outside a £300k home or a £2m home. Something memorable and instantly recognisable without being loud.
Should not have
• Clipart or stock-looking graphics. Busy layouts or too much text. Comic or playful styles. Generic swooshes, flames or racing stripes. Cheap-looking gradients. Bright colours that don't suit a premium brand. Low-resolution imagery. Designs that feel like a tradesman's van rather than a premium interiors company.

```html
<!DOCTYPE html>
<html lang="en">
<head>
<meta charset="utf-8">
<title>MERVALLE – TX. Mylo Cargo Wrap</title>
<link rel="stylesheet" href="https://fonts.googleapis.com/css2?family=Cinzel:wght@500&family=Roboto+Condensed:wght@500;700&display=swap">
<style>
  :root {
    --bg: #ffffff;
    --van-white: #f1f0ec;
    --van-shade: #dcdbd6;
    --navy: #0f1f45;
    --navy-deep: #0a1733;
    --silver: #a9adb5;
    --silver-light: #c9ccd1;
    --glass: #1c1f24;
    --tyre: #141414;
    --rim: #2a2a2a;
    --rim-light: #d8d8d8;
    --text-navy: #121c3a;
    --kitchen-light: #e4e1da;
    --kitchen-mid: #b9b2a6;
    --kitchen-floor: #8a6a4a;
  }
  * { margin: 0; padding: 0; box-sizing: border-box; }
  html, body { width: 1200px; height: 1200px; overflow: hidden; background: var(--bg); }
  .canvas { position: relative; width: 1200px; height: 1200px; }
  .van { position: absolute; inset: 0; width: 1200px; height: 1200px; }
  .services {
    position: absolute; left: 120px; top: 611px;
    font-family: "Roboto Condensed", sans-serif; font-weight: 700;
    font-size: 13px; letter-spacing: 0.2px; color: var(--text-navy);
  }
  .brand {
    position: absolute; left: 330px; top: 625px;
    display: flex; align-items: center; gap: 10px;
  }
  .brand-mark { width: 26px; height: 26px; background: var(--text-navy); }
  .brand-name {
    font-family: "Cinzel", serif; font-weight: 500;
    font-size: 30px; letter-spacing: 1px; color: var(--text-navy);
  }
  .offer {
    position: absolute; left: 402px; top: 675px;
    font-family: "Roboto Condensed", sans-serif; font-weight: 700;
    font-size: 18px; color: var(--text-navy);
  }
  .phone {
    position: absolute; left: 855px; top: 617px;
    font-family: "Roboto Condensed", sans-serif; font-weight: 700;
    font-size: 24px; letter-spacing: 0.5px; color: var(--text-navy);
  }
</style>
</head>
<body>
<div class="canvas">
  <svg class="van" viewBox="0 0 1200 1200" xmlns="http://www.w3.org/2000/svg">
    <defs>
      <clipPath id="body-clip">
        <path d="M40 800 L30 720 Q28 640 60 600 Q90 565 160 548 L250 470 Q330 405 420 400 L1060 400 Q1100 400 1110 420 L1150 520 Q1168 560 1170 620 L1172 760 Q1170 795 1150 800 Z"/>
      </clipPath>
      <linearGradient id="kitchen-fill" x1="0" y1="0" x2="0" y2="1">
        <stop offset="0" stop-color="var(--kitchen-light)"/>
        <stop offset="0.65" stop-color="var(--kitchen-mid)"/>
        <stop offset="1" stop-color="var(--kitchen-floor)"/>
      </linearGradient>
      <radialGradient id="ground-shadow">
        <stop offset="0" stop-color="#000" stop-opacity="0.25"/>
        <stop offset="1" stop-color="#000" stop-opacity="0"/>
      </radialGradient>
    </defs>

    <ellipse class="ground-shadow" cx="600" cy="860" rx="600" ry="22" fill="url(#ground-shadow)"/>

    <g clip-path="url(#body-clip)">
      <rect class="body-paint" x="0" y="380" width="1200" height="440" fill="var(--van-white)"/>
      <rect class="kitchen-image" x="580" y="400" width="600" height="410" fill="url(#kitchen-fill)" role="img" aria-label="Lifestyle photograph of a modern white kitchen with wood floor, blended into the rear body"/>
      <rect class="roof-shade" x="0" y="395" width="1200" height="16" fill="var(--van-shade)"/>
      <!-- grey accent band -->
      <path class="accent-silver" d="M95 640 C350 715 720 745 1070 590 L1072 606 C720 765 350 745 95 652 Z" fill="var(--silver)"/>
      <!-- navy band -->
      <path class="accent-navy" d="M110 662 C350 740 700 770 1065 612 L1068 648 C900 770 600 805 320 795 C230 770 165 710 110 662 Z" fill="var(--navy)"/>
      <path class="accent-silver-low" d="M300 790 C600 800 880 770 1068 660 L1070 672 C880 790 600 815 300 800 Z" fill="var(--silver-light)"/>
      <rect class="sill" x="0" y="790" width="1200" height="20" fill="var(--navy-deep)"/>
    </g>

    <!-- glazing -->
    <path class="windscreen" d="M175 545 L262 470 Q320 420 395 415 L370 540 Z" fill="var(--glass)"/>
    <path class="cab-window" d="M395 420 L570 420 L570 535 L372 540 Z" fill="var(--glass)"/>
    <path class="rear-windows" d="M582 414 L1010 414 Q1025 414 1020 440 L1015 510 Q1012 530 990 532 L582 532 Z" fill="var(--glass)" opacity="0.75"/>
    <path class="tail-glass" d="M1060 410 L1100 430 L1140 520 L1085 520 Z" fill="var(--glass)"/>
    <rect class="tail-light" x="1055" y="560" width="100" height="30" rx="10" fill="#3a0f12"/>
    <path class="headlight" d="M60 600 Q110 580 200 582 L195 600 Q120 600 70 615 Z" fill="#2d3036"/>
    <rect class="mirror" x="395" y="495" width="24" height="40" rx="8" fill="var(--glass)"/>

    <!-- panel lines -->
    <g class="panel-lines" stroke="#9a9a9a" stroke-width="1.5" fill="none">
      <line x1="318" y1="540" x2="318" y2="795"/>
      <line x1="578" y1="420" x2="578" y2="795"/>
    </g>
    <rect class="door-handle" x="510" y="592" width="44" height="12" rx="6" fill="#cfcfcf" stroke="#9a9a9a"/>

    <!-- wheels -->
    <g class="wheel wheel-front">
      <circle cx="212" cy="810" r="100" fill="var(--van-white)"/>
      <circle cx="212" cy="810" r="90" fill="var(--tyre)"/>
      <circle cx="212" cy="810" r="62" fill="var(--rim)"/>
      <circle cx="212" cy="810" r="58" fill="none" stroke="var(--rim-light)" stroke-width="6"/>
      <circle cx="212" cy="810" r="12" fill="var(--rim-light)"/>
    </g>
    <g class="wheel wheel-rear">
      <circle cx="962" cy="810" r="100" fill="var(--navy-deep)"/>
      <circle cx="962" cy="810" r="90" fill="var(--tyre)"/>
      <circle cx="962" cy="810" r="62" fill="var(--rim)"/>
      <circle cx="962" cy="810" r="58" fill="none" stroke="var(--rim-light)" stroke-width="6"/>
      <circle cx="962" cy="810" r="12" fill="var(--rim-light)"/>
    </g>
  </svg>

  <div class="services">• KITCHENS • BEDROOMS • BATHROOMS</div>
  <div class="brand">
    <span class="brand-mark"></span>
    <span class="brand-name">MERVALLE</span>
  </div>
  <div class="offer">Design | Supply | Install</div>
  <div class="phone">0123 456 789</div>
</div>
</body>
</html>
```